Q Linkra

Ned a new business card, need two designs one to be for communications and one to be for security.
Communications will have what we do on it which include:-
PABX systems
Data Cabling
Phone services
Fibre
Security
"your communications specialist in the Kestrel Coast"
The Severity one will have on it:-
CCTV
Alarm
Access control
Security consulting
Communications services
"Your security partner in the Kestrel Coast"
Target Market(s)
industry
Industry/Entity Type
Communications
Contact Information for Business Card
Bernard Colquist
0427309152
bernard@qlinkra.com.au
www.qlinkra.com.au

```html
<!DOCTYPE html>
<html lang="en">
<head>
<meta charset="utf-8">
<title>Q Linkra – Business Cards</title>
<link href="https://fonts.googleapis.com/css2?family=Open+Sans:wght@400;600;700&family=Caveat:wght@400&display=swap" rel="stylesheet">
<style>
  :root {
    --page-bg: #d9d9d9;
    --card-black: #050505;
    --band-dark: #141414;
    --accent: #f8ac3f;
    --rule-white: #f4f4f4;
    --text-light: #f2f2f2;
    --text-grey: #cfcfcf;
  }
  * { box-sizing: border-box; margin: 0; padding: 0; }
  html, body { width: 1200px; height: 900px; overflow: hidden; }
  body {
    background: var(--page-bg);
    font-family: "Open Sans", Arial, sans-serif;
    display: flex;
    flex-direction: column;
    align-items: center;
    justify-content: center;
    gap: 36px;
  }
  .card {
    position: relative;
    width: 700px;
    height: 400px;
    background: var(--card-black);
    overflow: hidden;
    box-shadow: 0 6px 18px rgba(0,0,0,0.25);
  }
  .card__band {
    position: absolute;
    left: 0; right: 0;
    top: 220px;
    height: 110px;
    background: var(--band-dark);
  }
  .card__rule {
    position: absolute;
    left: 0; right: 0;
    top: 330px;
    height: 9px;
    background: var(--rule-white);
  }
  .card__stripe {
    position: absolute;
    left: 0; right: 0;
    top: 339px;
    bottom: 0;
    background: var(--accent);
  }

  /* Front */
  .brand {
    position: absolute;
    left: 40px;
    top: 110px;
    display: flex;
    align-items: center;
    gap: 14px;
  }
  .brand__dot {
    width: 42px; height: 42px;
    border-radius: 50%;
    background: var(--accent);
  }
  .brand__name {
    font-weight: 700;
    font-size: 64px;
    line-height: 1;
    color: var(--accent);
    letter-spacing: 1px;
  }
  .holder {
    position: absolute;
    right: 42px;
    top: 104px;
    text-align: right;
  }
  .holder__name {
    font-weight: 600;
    font-size: 23px;
    color: var(--accent);
    letter-spacing: 0.5px;
    text-transform: uppercase;
  }
  .holder__role {
    font-size: 19px;
    color: var(--text-light);
  }
  .contact {
    position: absolute;
    top: 245px;
    font-size: 15.5px;
    line-height: 1.7;
    color: var(--text-light);
  }
  .contact--address { left: 40px; }
  .contact--phones { left: 300px; top: 262px; }
  .contact--web { left: 470px; top: 270px; }
  .contact__row { display: flex; align-items: center; gap: 7px; white-space: nowrap; }
  .icon { width: 14px; height: 14px; flex: none; fill: var(--accent); }

  /* Back */
  .back-brand {
    position: absolute;
    left: 0; right: 0;
    top: 70px;
    display: flex;
    justify-content: center;
    align-items: center;
    gap: 12px;
  }
  .back-brand__dot {
    width: 30px; height: 30px;
    border-radius: 50%;
    background: var(--accent);
  }
  .back-brand__name {
    font-weight: 700;
    font-size: 40px;
    color: var(--accent);
    line-height: 1;
  }
  .services {
    position: absolute;
    left: 0; right: 0;
    top: 150px;
    text-align: center;
    font-size: 17px;
    line-height: 1.5;
    color: var(--text-grey);
    word-spacing: 2px;
  }
  .tagline {
    position: absolute;
    left: 0; right: 0;
    top: 262px;
    text-align: center;
    font-family: "Caveat", cursive;
    font-size: 24px;
    color: var(--text-light);
    letter-spacing: 0.5px;
  }
</style>
</head>
<body>

  <section class="card card--back" aria-label="Business card back">
    <div class="card__band"></div>
    <div class="card__rule"></div>
    <div class="card__stripe"></div>
    <div class="back-brand">
      <span class="back-brand__dot"></span>
      <span class="back-brand__name">qlinkra</span>
    </div>
    <p class="services">PABX systems &nbsp;-&nbsp; Data Cabling &nbsp;-&nbsp; Phone services<br>Fibre &nbsp;-&nbsp; Security</p>
    <p class="tagline">"your communications specialist on the Kestrel Coast"</p>
  </section>

  <section class="card card--front" aria-label="Business card front">
    <div class="card__band"></div>
    <div class="card__rule"></div>
    <div class="card__stripe"></div>

    <div class="brand">
      <span class="brand__dot"></span>
      <span class="brand__name">qlinkra</span>
    </div>

    <div class="holder">
      <p class="holder__name">Bernard Colquist</p>
      <p class="holder__role">Managing Director</p>
    </div>

    <div class="contact contact--address">
      <p class="contact__row">
        <svg class="icon" viewBox="0 0 14 14"><path d="M7 0a5 5 0 0 0-5 5c0 3.6 5 9 5 9s5-5.4 5-9a5 5 0 0 0-5-5zm0 7a2 2 0 1 1 0-4 2 2 0 0 1 0 4z"/></svg>
        1234, Address Goes Here,
      </p>
      <p class="contact__row">Country Name, 123456</p>
    </div>

    <div class="contact contact--phones">
      <p class="contact__row">
        <svg class="icon" viewBox="0 0 14 14"><path d="M1 4c0-1.5 2-3 6-3s6 1.5 6 3v1.5h-3.5V4h-5v1.5H1z M3 7l1.5-1.5h5L11 7v5H3z"/></svg>
        123.456.7890
      </p>
      <p class="contact__row">
        <svg class="icon" viewBox="0 0 14 14"><path d="M3 1h6v4H3z M1 5h12v8H1z M3 7v2h2V7z M6 7v2h2V7z"/></svg>
        123.456.7890
      </p>
    </div>

    <div class="contact contact--web">
      <p class="contact__row">
        <svg class="icon" viewBox="0 0 14 14"><path d="M1 3h12v8H1z"/><path d="M1 3l6 5 6-5" fill="none" stroke="#141414" stroke-width="1.2"/></svg>
        bernard@qlinkra.com.au
      </p>
      <p class="contact__row">
        <svg class="icon" viewBox="0 0 14 14"><path d="M5.5 8.5l3-3" stroke="#f8ac3f" stroke-width="1.6" fill="none"/><path d="M6 4l1.5-1.5a2.5 2.5 0 0 1 3.5 3.5L9.5 7.5M8 10l-1.5 1.5a2.5 2.5 0 0 1-3.5-3.5L4.5 6.5" stroke="#f8ac3f" stroke-width="1.6" fill="none"/></svg>
        www.qlinkra.com.au
      </p>
    </div>
  </section>

</body>
</html>
```